Professional Business Card for Commercial Cleaning Company

We need a business card that represents our commercial janitorial cleaning company and represent several brands for our company so we do not want to highlight the logo too much. We want something that says we are professional.
Notes:No website or address as we have many locations and many websites and companies under our corporate name of "Brightvale Holdings, LLC" . Every time we hand a customer a business card they have contacted us via another brand we own but we don't want to have 21 business cards so we want to not focus on Brightvale Holdings, LLC too much since people will automatically ask "What is Brightvale Holdings, LLC" Example: Noodle Barn and Wrap Lantern restaurants are owned by "Zest! Brands" is the corporation name. Same principle here. Except we do not advertise at this time that all of our brands are connected. Hope this helps.
Target Market(s)
Commercial Cleaning
Industry/Entity Type
Janitorial Service
Contact Information for Business Card
Milo Jarvis
Business Development
555-382-9047
sales@brightvaleholdingsllc.example
Requirements
Must have
- Logo with contact information, need to be able to easily edit contact info for others in my office.
Nice to have
- Professional Image. Like to see a colorful bold look and a more standard business card look.
Should not have
- Any type of cleaning icons, tools, people or water.

```html
<!DOCTYPE html>
<html lang="en">
<head>
<meta charset="UTF-8">
<title>Brightvale Holdings, LLC — Business Card</title>
<link rel="stylesheet" href="https://fonts.googleapis.com/css2?family=Montserrat:wght@600;700&family=Roboto:wght@400;500;700&display=swap">
<style>
  :root {
    --navy: #0a3a80;
    --navy-deep: #062f6b;
    --green: #4f9a2b;
    --ink: #2d3440;
    --paper: #f4f4f5;
    --stage: #e9ecee;
    --rule: #9aa0a8;
  }
  * { box-sizing: border-box; margin: 0; padding: 0; }
  html, body { width: 1200px; height: 900px; overflow: hidden; }
  body {
    background: var(--stage);
    display: flex;
    flex-direction: column;
    align-items: center;
    justify-content: center;
    gap: 48px;
    font-family: "Roboto", Arial, sans-serif;
  }
  .card {
    width: 630px;
    height: 360px;
    border-radius: 4px;
    box-shadow: 0 10px 28px rgba(20, 40, 70, 0.16);
    position: relative;
  }
  .card--front {
    background: linear-gradient(160deg, var(--navy) 0%, var(--navy-deep) 100%);
    display: flex;
    align-items: center;
    justify-content: center;
  }
  .wordmark {
    font-family: "Montserrat", Arial, sans-serif;
    font-weight: 700;
    letter-spacing: 0.2px;
  }
  .card--front .wordmark { color: #ffffff; font-size: 34px; }
  .card--back {
    background: var(--paper);
    display: flex;
    align-items: center;
  }
  .card--back .brand {
    width: 330px;
    display: flex;
    justify-content: center;
  }
  .card--back .wordmark { color: var(--navy); font-size: 22px; }
  .divider {
    width: 1px;
    height: 110px;
    background: var(--rule);
  }
  .contact {
    padding-left: 26px;
    display: flex;
    flex-direction: column;
  }
  .contact__name {
    color: var(--navy);
    font-weight: 700;
    font-size: 24px;
    line-height: 1.1;
  }
  .contact__title {
    color: var(--green);
    font-weight: 500;
    font-size: 15px;
    margin-bottom: 12px;
  }
  .contact__line {
    display: flex;
    align-items: center;
    gap: 8px;
    color: var(--ink);
    font-size: 13px;
    line-height: 1.6;
  }
  .contact__icon { width: 12px; height: 12px; flex: none; }
</style>
</head>
<body>
  <section class="card card--front" aria-label="Card front">
    <span class="wordmark">Brightvale Holdings, LLC</span>
  </section>

  <section class="card card--back" aria-label="Card back">
    <div class="brand"><span class="wordmark">Brightvale Holdings, LLC</span></div>
    <div class="divider"></div>
    <div class="contact">
      <span class="contact__name">Milo Jarvis</span>
      <span class="contact__title">Business Development</span>
      <span class="contact__line">
        <svg class="contact__icon" viewBox="0 0 12 12" aria-hidden="true">
          <rect x="3" y="0.8" width="6" height="10.4" rx="1" fill="none" stroke="var(--navy)" stroke-width="1.3"/>
          <line x1="5" y1="9.2" x2="7" y2="9.2" stroke="var(--navy)" stroke-width="1"/>
        </svg>
        555-382-9047
      </span>
      <span class="contact__line">
        <svg class="contact__icon" viewBox="0 0 12 12" aria-hidden="true">
          <rect x="0.5" y="2" width="11" height="8" rx="1" fill="var(--navy)"/>
          <polyline points="1,2.8 6,6.6 11,2.8" fill="none" stroke="#ffffff" stroke-width="1"/>
        </svg>
        sales@brightvaleholdingsllc.example
      </span>
    </div>
  </section>
</body>
</html>
```